Customer Dashboard Design for Email Security SaaS

Mailbrook is a commercial email spam filter offered as a SaaS product, built and operated by a small German hosting provider. It protects business email accounts against spam, phishing, scam, and viruses using a multilayer filtering pipeline that combines traditional spam detection with AI-powered classification. The product runs entirely on German infrastructure, ensuring data sovereignty for European customers.

We need a complete redesign of the customer-facing dashboard. This is the web application where paying customers manage their email filtering: view their mail log, check quarantined emails, manage allow/blocklists, configure their settings, and handle their subscription. It is the primary touchpoint between Mailbrook and its customers.

Our customers are system administrators, IT managers at small-to-medium businesses, and operators of small hosting providers. They are technically competent but not designers. They expect professional, efficient tools that respect their time. They typically manage 10–500 email accounts and check the dashboard a few times per week, with heavier use during spam incidents.

We have attached the current mockups which really need to be replaced with something good looking.

Target Market(s)

System administrators, IT managers at small-to-medium businesses, and operators of small hosting providers.

Industry/Entity Type

SaaS

Number of Pages Required

5+ page

```html
<!DOCTYPE html>
<html lang="de">
<head>
<meta charset="utf-8">
<title>Mailbrook – Blocklist</title>
<link href="https://fonts.googleapis.com/css2?family=Inter:wght@400;500;600;700&display=swap" rel="stylesheet">
<style>
:root{
  --bg:#f3f2ef;
  --surface:#ffffff;
  --line:#ebe9e4;
  --ink:#1c1f2a;
  --muted:#5f6470;
  --faint:#9a9ea6;
  --green:#3b8a5c;
  --red:#cf4a4e;
  --red-soft:#f6eae9;
  --red-tint:#f3e8e7;
  --red-border:#dc8a8b;
  --red-btn:#e6aeae;
}
*{box-sizing:border-box;margin:0;padding:0}
html,body{width:1200px;height:955px;overflow:hidden}
body{font-family:"Inter",sans-serif;background:var(--bg);color:var(--ink);position:relative}
svg{display:block}
.sidebar{position:absolute;left:0;top:0;width:209px;height:955px;background:var(--surface);border-right:1px solid var(--line)}
.brand{height:52px;border-bottom:1px solid var(--line);display:flex;align-items:center;padding-left:16px;gap:10px}
.brand-mark{width:33px;height:33px;border-radius:8px;background:var(--green)}
.brand-name{font-size:15px;font-weight:600}
.nav{padding:0 10px;margin-top:21px}
.nav-item{height:36px;margin-bottom:6.6px;border-radius:8px;display:flex;align-items:center;padding-left:10px;gap:12px;font-size:12.5px;color:#3d424d}
.nav-item svg{width:17px;height:17px;stroke:#4a4f5a;fill:none;stroke-width:1.7;stroke-linecap:round;stroke-linejoin:round}
.nav-item.active{background:var(--green);color:#fff;font-weight:500}
.nav-item.active svg{stroke:#fff}
.sidebar-foot{position:absolute;left:0;right:0;top:813px;border-top:1px solid var(--line);padding:0 10px}
.theme{height:48px}
.user-card{border:1px solid #e3e1dc;background:#f7f6f3;border-radius:8px;height:80px;padding:12px 10px}
.user{display:flex;align-items:center;gap:8px}
.avatar{width:27px;height:27px;border-radius:50%;background:var(--green);color:#fff;font-size:10px;font-weight:600;display:flex;align-items:center;justify-content:center}
.user-name{font-size:12.5px;font-weight:500}
.user-mail{font-size:10.5px;color:var(--faint)}
.logout{display:flex;align-items:center;gap:9px;margin-top:10px;padding-left:8px;font-size:10.5px;color:#4a4f5a}
.logout svg{width:13px;height:13px;stroke:#4a4f5a;fill:none;stroke-width:1.7;stroke-linecap:round;stroke-linejoin:round}
.main{position:absolute;left:321px;top:0;width:767px}
h1{font-size:31px;font-weight:600;letter-spacing:-.5px;margin-top:28px;line-height:34px}
.lead{font-size:13.4px;color:var(--muted);line-height:20px;margin-top:8px}
.info{margin-top:15px;height:64px;border:1px solid var(--red-border);background:var(--red-tint);border-radius:10px;display:flex;align-items:center;padding:0 14px 0 13px;gap:10px}
.info-icon{width:26px;height:26px;border-radius:6px;background:var(--red);display:flex;align-items:center;justify-content:center}
.info-icon svg{width:15px;height:15px;stroke:#fff;fill:none;stroke-width:1.8;stroke-linecap:round;stroke-linejoin:round}
.info-title{font-size:12px;font-weight:500}
.info-sub{font-size:11.8px;color:var(--muted);margin-top:6px}
.info .chev{margin-left:auto;width:13px;height:13px;stroke:#8a8e96;fill:none;stroke-width:1.6}
.card{background:var(--surface);border-radius:11px}
.add{margin-top:21px;height:147px;padding:20px 17px}
.card-title{font-size:15.5px;color:#8b8f97;font-weight:500;letter-spacing:-.3px}
.toggle{display:flex;gap:7px;margin-top:13px}
.toggle div{flex:1;height:34px;border-radius:6px;border:1px solid #e1dfda;display:flex;align-items:center;justify-content:center;font-size:12px;color:#3d424d}
.toggle .on{background:var(--red-soft);border-color:var(--red-border);color:var(--red)}
.input-row{display:flex;gap:8px;margin-top:10px}
.input{flex:1;height:37px;border:1px solid #e1dfda;border-radius:6px;display:flex;align-items:center;padding-left:13px;font-size:13.5px;color:#8b8f97}
.btn{width:124px;height:32px;margin-top:2.5px;border-radius:16px;background:var(--red-btn);color:#fff;font-size:14px;font-weight:500;display:flex;align-items:center;justify-content:center;gap:7px}
.btn svg{width:12px;height:12px;stroke:#fff;stroke-width:1.6}
.list{margin-top:22px;overflow:hidden}
.list-head{height:53px;padding:0 17px;display:flex;align-items:center;border-bottom:1px solid var(--line)}
.entry{height:63px;display:flex;align-items:center;padding:0 20px 0 13px}
.entry + .entry{border-top:1px solid var(--line);background:#faf9f7}
.entry-name{font-size:14px;font-weight:500;display:flex;align-items:center;gap:10px}
.tag{font-size:10px;font-weight:500;color:var(--red);background:var(--red-soft);border-radius:8px;padding:3px 7px}
.entry-date{font-size:10.3px;color:var(--faint);margin-top:6px}
.trash{margin-left:auto;width:14px;height:14px;stroke:var(--red);fill:none;stroke-width:1.7;stroke-linecap:round;stroke-linejoin:round}
</style>
</head>
<body>
<aside class="sidebar">
  <div class="brand"><span class="brand-mark"></span><span class="brand-name">Mailbrook</span></div>
  <nav class="nav">
    <div class="nav-item"><svg viewBox="0 0 24 24"><rect x="3" y="3" width="7" height="9" rx="1"/><rect x="14" y="3" width="7" height="5" rx="1"/><rect x="14" y="12" width="7" height="9" rx="1"/><rect x="3" y="16" width="7" height="5" rx="1"/></svg>Dashboard</div>
    <div class="nav-item"><svg viewBox="0 0 24 24"><rect x="2" y="4" width="20" height="16" rx="2"/><path d="m22 7-10 6L2 7"/></svg>Mail-Log</div>
    <div class="nav-item"><svg viewBox="0 0 24 24"><path d="M22 12h-6l-2 3h-4l-2-3H2"/><path d="M5.5 5h13L22 12v6a2 2 0 0 1-2 2H4a2 2 0 0 1-2-2v-6z"/></svg>Postfächer</div>
    <div class="nav-item"><svg viewBox="0 0 24 24"><path d="M12 22s8-3.5 8-10V5l-8-3-8 3v7c0 6.5 8 10 8 10z"/><path d="m9 12 2 2 4-4"/></svg>Allowlist</div>
    <div class="nav-item active"><svg viewBox="0 0 24 24"><path d="M12 22s8-3.5 8-10V5l-8-3-8 3v7c0 6.5 8 10 8 10z"/><path d="m9.5 9.5 5 5m0-5-5 5"/></svg>Blocklist</div>
    <div class="nav-item"><svg viewBox="0 0 24 24"><rect x="4" y="11" width="16" height="10" rx="2"/><path d="M8 11V7a4 4 0 0 1 8 0v4"/></svg>Quarantäne</div>
    <div class="nav-item"><svg viewBox="0 0 24 24"><circle cx="12" cy="12" r="3"/><path d="M19.4 15a1.7 1.7 0 0 0 .3 1.8l.1.1a2 2 0 1 1-2.8 2.8l-.1-.1a1.7 1.7 0 0 0-2.9 1.2V21a2 2 0 1 1-4 0v-.1a1.7 1.7 0 0 0-2.9-1.2l-.1.1a2 2 0 1 1-2.8-2.8l.1-.1A1.7 1.7 0 0 0 3 14H3a2 2 0 1 1 0-4h.1a1.7 1.7 0 0 0 1.2-2.9l-.1-.1a2 2 0 1 1 2.8-2.8l.1.1A1.7 1.7 0 0 0 10 3V3a2 2 0 1 1 4 0v.1a1.7 1.7 0 0 0 2.9 1.2l.1-.1a2 2 0 1 1 2.8 2.8l-.1.1A1.7 1.7 0 0 0 21 10h.1a2 2 0 1 1 0 4H21a1.7 1.7 0 0 0-1.6 1z"/></svg>Einstellungen</div>
    <div class="nav-item"><svg viewBox="0 0 24 24"><rect x="2" y="5" width="20" height="14" rx="2"/><path d="M2 10h20"/></svg>Abrechnung</div>
  </nav>
  <div class="sidebar-foot">
    <div class="nav-item theme"><svg viewBox="0 0 24 24"><path d="M21 12.8A9 9 0 1 1 11.2 3 7 7 0 0 0 21 12.8z"/></svg>Dunkel</div>
    <div class="user-card">
      <div class="user"><span class="avatar">JK</span><div><div class="user-name">Jonas Keller</div><div class="user-mail">admin@example.de</div></div></div>
      <div class="logout"><svg viewBox="0 0 24 24"><path d="M9 21H5a2 2 0 0 1-2-2V5a2 2 0 0 1 2-2h4"/><path d="m16 17 5-5-5-5M21 12H9"/></svg>Abmelden</div>
    </div>
  </div>
</aside>

<main class="main">
  <h1>Blocklist</h1>
  <p class="lead">E-Mails von Absendern auf der Blocklist werden grundsätzlich abgelehnt, unabhängig vom Ergebnis des Spamfilters.<br>Nutzen Sie diese Liste für bekannte Spam-Quellen oder unerwünschte Absender.</p>

  <div class="info">
    <span class="info-icon"><svg viewBox="0 0 24 24"><path d="M12 22s8-3.5 8-10V5l-8-3-8 3v7c0 6.5 8 10 8 10z"/><path d="m9.5 9.5 5 5m0-5-5 5"/></svg></span>
    <div><div class="info-title">Was bedeuten die Eintragstypen?</div><div class="info-sub">Klicken Sie hier für weitere Informationen</div></div>
    <svg class="chev" viewBox="0 0 24 24"><path d="m6 9 6 6 6-6"/></svg>
  </div>

  <section class="card add">
    <div class="card-title">EINTRAG HINZUFÜGEN</div>
    <div class="toggle"><div class="on">E-Mail-Adresse</div><div>Absender-Domain</div></div>
    <div class="input-row">
      <div class="input">z.B. spam@spam-schleuder.test</div>
      <div class="btn"><svg viewBox="0 0 12 12"><path d="M6 1v10M1 6h10"/></svg>Hinzufügen</div>
    </div>
  </section>

  <section class="card list">
    <div class="list-head"><div class="card-title">EINTRÄGE (2)</div></div>
    <div class="entry">
      <div><div class="entry-name">bulk-sender.test <span class="tag">Domain</span></div><div class="entry-date">Hinzugefügt am 08.02.2026</div></div>
      <svg class="trash" viewBox="0 0 24 24"><path d="M3 6h18M8 6V4h8v2M6 6l1 15h10l1-15M10 11v6M14 11v6"/></svg>
    </div>
    <div class="entry">
      <div><div class="entry-name">phishing@scam.test <span class="tag">E-Mail</span></div><div class="entry-date">Hinzugefügt am 12.02.2026</div></div>
      <svg class="trash" viewBox="0 0 24 24"><path d="M3 6h18M8 6V4h8v2M6 6l1 15h10l1-15M10 11v6M14 11v6"/></svg>
    </div>
  </section>
</main>
</body>
</html>
```